Inspiring Poster for Company Staff Room

What we need:
We want an awesome design to create a poster that will be plaque mounted in our staff room. We just went through a very motivating workshop to discover our "WHY" as a company...basically, to define the reason we are in business, and to define what motivates us to come to work every day. The poster must be motivating but really resonate with our team…we are not looking for a “typical” motivational poster that we can purchase off Amazon!

Who we are:
We are a property management company, a team of 20 that is passionate about our investors, and residents who rent from us, but more importantly, we love helping people and making a difference in our industry. We are proud and work hard for every single 5 star Google review we achieve.

Information for you:
We have included a mock up of the poster, which words we want, and the placement of them (in a general sense) but we need a designer to really bring this together in an inspiring poster that represents our company’s culture, feel, and fit. We have also included a logo file, as well as examples of our business cards, letterhead and thank you card already designed.
Here are the parameters:

(1) Poster size: 24” x 36”
(2) Full colour
(3) Must incorporate our company logo
(4) Must incorporate the following words:

Why do I come to work?

“To feel fulfilled by empathizing, educating and empowering our clients and co-workers so that we can build strong, impactful relationships”

Own the outcome

(5) Please see our website at www.brindlecovepm.com to get a feel for our company culture and for a better idea of our current company graphics

Target Market(s)

Our staff. Will not be seen by our clients

Industry/Entity Type

Real Estate

Font styles to use
Serif
Sans Serif

Requirements
Should not have
• Would not want this to be too "busy." if you can picture it, the poster will be mounted on the wall as soon as someone enters the room. The idea is to remind them each day why they come to work.

```html
<!DOCTYPE html>
<html lang="en">
<head>
<meta charset="utf-8">
<title>Why We Come to Work – Brindle Cove Property Management</title>
<link href="https://fonts.googleapis.com/css2?family=League+Spartan:wght@700;900&family=Montserrat:wght@900&display=swap" rel="stylesheet">
<style>
  :root {
    --paper: #f8f4ed;
    --margin: #ffffff;
    --navy-blue: #41719f;
    --sky-blue: #99c9ec;
    --brand-blue: #3497cf;
  }
  * { margin: 0; padding: 0; box-sizing: border-box; }
  html, body {
    width: 849px;
    height: 1200px;
    overflow: hidden;
    background: var(--margin);
  }
  .poster {
    position: relative;
    width: 849px;
    height: 1200px;
    background: var(--margin);
  }
  .poster__sheet {
    position: absolute;
    left: 24px;
    right: 24px;
    top: 0;
    bottom: 0;
    background: var(--paper);
  }
  .brand {
    position: absolute;
    top: 56px;
    left: 0;
    right: 0;
    display: flex;
    justify-content: center;
    align-items: center;
    gap: 12px;
  }
  .brand__square {
    width: 34px;
    height: 34px;
    background: var(--brand-blue);
  }
  .brand__name {
    font-family: "League Spartan", sans-serif;
    font-weight: 700;
    color: var(--brand-blue);
    text-transform: uppercase;
    line-height: 1;
  }
  .brand__name-main {
    display: block;
    font-size: 27px;
    letter-spacing: 1px;
  }
  .brand__name-sub {
    display: block;
    font-size: 10px;
    letter-spacing: 2.6px;
    margin-top: 3px;
  }
  .headline {
    position: absolute;
    top: 228px;
    left: 0;
    right: 0;
    text-align: center;
    font-family: "Montserrat", sans-serif;
    font-weight: 900;
    font-size: 190px;
    line-height: 1;
    letter-spacing: -4px;
    color: var(--navy-blue);
  }
  .purpose {
    position: absolute;
    top: 482px;
    left: 0;
    right: 0;
    text-align: center;
    font-family: "League Spartan", sans-serif;
    font-weight: 700;
    font-size: 47px;
    line-height: 46px;
    text-transform: uppercase;
    white-space: nowrap;
    color: var(--navy-blue);
  }
  .purpose__soft { color: var(--sky-blue); }
  .motto {
    position: absolute;
    top: 1068px;
    left: 0;
    right: 0;
    text-align: center;
    font-family: "League Spartan", sans-serif;
    font-weight: 700;
    font-size: 47px;
    line-height: 1;
    text-transform: uppercase;
    color: var(--navy-blue);
  }
</style>
</head>
<body>
  <main class="poster">
    <div class="poster__sheet">
      <header class="brand">
        <span class="brand__square" aria-hidden="true"></span>
        <p class="brand__name">
          <span class="brand__name-main">Brindle Cove</span>
          <span class="brand__name-sub">Property Management</span>
        </p>
      </header>

      <h1 class="headline">WHY?</h1>

      <p class="purpose">
        <span class="purpose__soft">To feel</span> fulfilled <span class="purpose__soft">by</span><br>
        empathizing, educating and<br>
        empowering <span class="purpose__soft">our clients</span><br>
        <span class="purpose__soft">and co-workers so that we</span><br>
        <span class="purpose__soft">can build</span> strong, impactful<br>
        relationships.
      </p>

      <p class="motto">Own the outcome</p>
    </div>
  </main>
</body>
</html>
```